Website for Excavator and Earthworks Company

We require a modern, sleek and practical website for our newly created earthworks/excavator business in Perth, Western Australia called Kolbane Ridge Earthworks.

The website should have a modern, cutting edge feel but only needs to be relatively simplistic in it's layout and eventual functionality.

Some pages it should have would be Home, About, Projects and Contact Us.

```html
<!DOCTYPE html>
<html lang="en">
<head>
<meta charset="utf-8">
<title>Kolbane Ridge Earthworks</title>
<link href="https://fonts.googleapis.com/css2?family=Krona+One&family=Lato:wght@300;400;700;900&family=Roboto:wght@500&display=swap" rel="stylesheet">
<style>
:root{
  --lime:#c8dc00;
  --ink:#111111;
  --grey:#e7e7e5;
  --text:#555555;
  --footer:#1b1b1a;
  --white:#ffffff;
}
*{box-sizing:border-box;margin:0;padding:0}
html,body{width:1200px;height:4029px;overflow:hidden;background:var(--white)}
body{position:relative;font-family:"Lato",sans-serif;color:var(--ink)}
a{text-decoration:none}
.abs{position:absolute}
.display{font-family:"Krona One",sans-serif;font-weight:400;letter-spacing:0.5px}
.accent{color:var(--lime)}
.btn{position:absolute;display:flex;align-items:center;justify-content:flex-start;padding-left:14px;font-weight:700;font-size:16px;color:var(--ink);background:var(--lime);text-decoration:none;clip-path:polygon(0 0,86% 0,100% 50%,86% 100%,0 100%)}
.photo{position:absolute}
.header{position:absolute;left:0;top:0;width:1200px;height:80px;background:var(--white)}
.brand{position:absolute;display:flex;align-items:center;gap:12px;font-family:"Krona One",sans-serif;font-size:24px;color:var(--ink)}
.brand-mark{width:40px;height:40px;background:var(--lime)}
.nav a{position:absolute;font-size:16px;color:#333}
.nav .home{left:679px;top:19px;width:66px;height:34px;background:var(--ink);color:#fff;font-weight:700;display:flex;align-items:center;justify-content:center;clip-path:polygon(0 0,86% 0,100% 50%,86% 100%,0 100%)}
.hero{position:absolute;left:0;top:80px;width:1200px;height:622px;background:var(--grey);overflow:hidden}
.hero h1{position:absolute;left:110px;top:138px;font-size:38px;line-height:58px;font-weight:400}
.hero p{position:absolute;left:110px;top:388px;width:480px;font-size:20px;line-height:32px;color:var(--text)}
.sec-title{position:absolute;font-size:38px;text-align:center;width:1200px;left:0}
.eyebrow{position:absolute;display:flex;align-items:center;gap:16px;font-size:17px;font-weight:700;letter-spacing:0.5px}
.eyebrow::before,.eyebrow::after{content:"";width:80px;height:3px;background:var(--lime)}
.card{position:absolute;top:904px;width:316px;height:404px;background:#fff;box-shadow:0 2px 10px rgba(0,0,0,.15)}
.card .photo{left:9px;top:10px;width:298px;height:325px}
.card h3{position:absolute;left:0;width:100%;text-align:center;font-weight:500;font-size:22px;top:355px}
.card.active{background:var(--lime)}
.card.active h3{top:290px}
.card.active p{position:absolute;top:330px;width:100%;text-align:center;font-size:14px;color:#555;font-weight:300}
.arrow-btn{position:absolute;top:1100px;width:26px;height:26px;border-radius:50%}
.why{position:absolute;left:0;top:1403px;width:1200px;height:482px;background:var(--grey);overflow:hidden}
.benefit{position:absolute;left:713px;display:flex;align-items:center;gap:20px;font-size:16px;color:#444}
.benefit i{width:44px;height:44px;border-radius:50%;background:var(--lime);display:flex;align-items:center;justify-content:center}
.about p{position:absolute;left:111px;width:443px;font-size:12.5px;line-height:27px;color:#444;text-align:justify}
.cta{position:absolute;left:110px;top:2502px;width:980px;height:430px;background:linear-gradient(180deg,#2f5f9a 0%,#5f86b0 45%,#8d6b45 75%,#5b4430 100%)}
.cta h2{position:absolute;left:0;top:140px;width:100%;text-align:center;color:#fff;font-size:38px;line-height:56px}
.cta p{position:absolute;left:0;top:253px;width:100%;text-align:center;color:#f0ef9e;font-size:17px;font-weight:700}
.footer{position:absolute;left:0;top:3647px;width:1200px;height:382px;background:var(--footer);color:#fff}
.footer h4{position:absolute;color:var(--lime);font-size:19px;font-weight:700}
.footer ul{position:absolute;list-style:none;font-size:13px;line-height:31px}
.contact-row{position:absolute;left:889px;display:flex;align-items:center;gap:16px;font-size:13px}
.contact-row i{width:22px;height:22px;background:#fff;border-radius:4px;display:flex;align-items:center;justify-content:center}
.social{position:absolute;top:3940px;width:24px;height:24px;background:#fff;border-radius:3px}
</style>
</head>
<body>

<header class="header">
  <div class="brand" style="left:110px;top:20px"><span class="brand-mark"></span>Kolbane Ridge</div>
  <nav class="nav">
    <a class="home" href="#">Home</a>
    <a href="#" style="left:778px;top:27px">About</a>
    <a href="#" style="left:867px;top:27px">Projects</a>
    <a class="btn" href="#" style="left:972px;top:17px;width:115px;height:47px">CONTACT</a>
  </nav>
</header>

<section class="hero">
  <svg class="abs" style="left:0;top:0" width="1200" height="622" viewBox="0 0 1200 622">
    <defs>
      <linearGradient id="heroSky" x1="0" y1="0" x2="0" y2="1">
        <stop offset="0" stop-color="#4b6f98"/><stop offset="0.45" stop-color="#9bb4cc"/>
        <stop offset="0.6" stop-color="#d7a23a"/><stop offset="1" stop-color="#8a5432"/>
      </linearGradient>
    </defs>
    <polygon points="538,0 560,0 670,311 560,622 538,622 648,311" fill="var(--lime)"/>
    <polygon role="img" aria-label="Yellow excavator digging red earth under a cloudy sky" points="555,0 1200,0 1200,622 555,622 665,311" fill="url(#heroSky)"/>
  </svg>
  <h1 class="display">RELIABLE<br><span class="accent">EXCAVATION &amp;<br>EARTH MOVING</span><br>SOLUTIONS</h1>
  <p>Precision excavation, site preparation and earthmoving solutions across Western Australia.</p>
  <a class="btn" href="#" style="left:110px;top:469px;width:133px;height:47px;font-size:15px">GET A QUOTE</a>
</section>

<h2 class="sec-title display" style="top:784px">What <span class="accent">We Do</span></h2>
<div class="eyebrow" style="left:463px;top:848px">SERVICES</div>

<span class="arrow-btn" style="left:35px;background:var(--lime)"></span>
<span class="arrow-btn" style="left:1124px;background:#d4d4d4"></span>

<div class="card" style="left:111px">
  <div class="photo" role="img" aria-label="Two workers in orange gear walking toward haul trucks in an open-cut mine" style="background:linear-gradient(180deg,#8b96a0,#5d5f5c 55%,#3c3c3a)"></div>
  <h3>Excavation</h3>
</div>
<div class="card active" style="left:441px">
  <div class="photo" role="img" aria-label="Excavator laying a large black pipe in a trench" style="height:215px;background:linear-gradient(180deg,#4f86c4,#b49a74 60%,#8a6a48);clip-path:polygon(0 0,100% 0,100% 85%,55% 100%,0 70%)"></div>
  <svg class="abs" style="left:128px;top:202px" width="56" height="56" viewBox="0 0 56 56"><circle cx="28" cy="28" r="27" fill="var(--lime)"/><path d="M17 35h22M20 30v-8h6v8M30 22h6v8M19 40h18" stroke="#111" stroke-width="2.5" fill="none"/></svg>
  <h3>Trenching &amp; Drainage</h3>
  <p>Utility trenches and drainage systems.</p>
</div>
<div class="card" style="left:770px">
  <div class="photo" role="img" aria-label="Excavator clearing burning scrub in bushland" style="background:linear-gradient(180deg,#9cc0e4,#b9b6a6 45%,#6e7a3c 75%,#5e4a30)"></div>
  <h3>Land Clearing</h3>
</div>

<section class="why">
  <svg class="abs" style="left:0;top:0" width="700" height="482" viewBox="0 0 700 482">
    <defs><linearGradient id="cab" x1="0" y1="0" x2="1" y2="1"><stop offset="0" stop-color="#3d4450"/><stop offset="0.6" stop-color="#c9a23a"/><stop offset="1" stop-color="#5a5a52"/></linearGradient></defs>
    <polygon points="657,0 673,0 585,482 569,482" fill="var(--lime)"/>
    <polygon role="img" aria-label="Smiling operator in hard hat giving thumbs up from an excavator cab" points="0,0 672,0 580,470 0,470" fill="url(#cab)"/>
  </svg>
  <h2 class="display abs" style="left:707px;top:60px;font-size:36px">Why <span class="accent">Choose Us</span></h2>
  <div class="eyebrow" style="left:713px;top:124px">BENEFITS</div>
  <div class="benefit" style="top:171px"><i><svg width="20" height="20" viewBox="0 0 20 20"><path d="M3 15h10M5 15v-5h6v5M11 10l5-5" stroke="#111" stroke-width="2" fill="none"/></svg></i>Modern Equipment Fleet</div>
  <div class="benefit" style="top:225px"><i><svg width="20" height="20" viewBox="0 0 20 20"><circle cx="10" cy="7" r="3.5" fill="#111"/><path d="M3 18c1-5 13-5 14 0z" fill="#111"/></svg></i>Experienced Operators</div>
  <div class="benefit" style="top:282px"><i><svg width="20" height="20" viewBox="0 0 20 20"><path d="M10 2l7 3v5c0 4-3 7-7 8-4-1-7-4-7-8V5z" fill="#111"/><path d="M7 10l2 2 4-4" stroke="var(--lime)" stroke-width="2" fill="none"/></svg></i>Safety Focused</div>
  <div class="benefit" style="top:343px"><i><svg width="20" height="20" viewBox="0 0 20 20"><circle cx="10" cy="10" r="7" stroke="#111" stroke-width="2" fill="none"/><path d="M10 6v4l3 2" stroke="#111" stroke-width="2" fill="none"/></svg></i>Reliable Scheduling</div>
  <div class="benefit" style="top:396px"><i><svg width="20" height="20" viewBox="0 0 20 20"><path d="M3 11l8-8h6v6l-8 8z" fill="#111"/><circle cx="14" cy="6" r="1.5" fill="var(--lime)"/></svg></i>Competitive Pricing</div>
</section>

<section class="about">
  <h2 class="display abs" style="left:113px;top:1992px;font-size:36px">Who <span class="accent">We Are</span></h2>
  <div class="eyebrow" style="left:113px;top:2056px">ABOUT US</div>
  <p style="top:2098px">At Kolbane Ridge Earthworks, we treat every project as a reflection of our reputation. We are committed to delivering clean job sites, precise results, and dependable service from the first consultation to final handover.</p>
  <p style="top:2218px">Our mission is simple — to deliver dependable earthmoving solutions while building long-term relationships based on trust, performance, and quality workmanship.</p>
  <a class="btn" href="#" style="left:111px;top:2325px;width:135px;height:47px">READ MORE</a>
  <div class="photo" role="img" aria-label="Engineer and site worker in hard hats reviewing plans beside an excavator" style="left:745px;top:2000px;width:344px;height:416px;background:linear-gradient(180deg,#7a6a55,#b0884e 55%,#5a3f28)"></div>
  <div class="photo" role="img" aria-label="Excavator bucket over a mound of earth against blue sky" style="left:646px;top:2173px;width:293px;height:243px;background:linear-gradient(180deg,#6fa5d8,#a9c7e2 50%,#b97a45 75%,#8a5630);outline:6px solid #fff"></div>
</section>

<section class="cta" role="img" aria-label="Excavator working on a cleared site under blue sky">
  <h2 class="display">Let’s Build Strong<br>Foundations Together</h2>
  <p>From First Dig To Final Grade — We’ve Got You Covered</p>
  <a class="btn" href="#" style="left:405px;top:300px;width:167px;height:47px">BOOK YOUR JOB</a>
</section>

<h2 class="sec-title display" style="top:3006px">Our <span class="accent">Projects</span></h2>
<div class="eyebrow" style="left:461px;top:3065px">GALLERY</div>

<div class="photo" role="img" aria-label="Aerial view of excavators and trucks in a sandy pit" style="left:102px;top:3128px;width:444px;height:414px;background:linear-gradient(180deg,#a89f8a,#c3b79a 45%,#d6d87a 75%,var(--lime))">
  <span class="abs" style="left:50px;top:362px;font-family:'Roboto',sans-serif;font-weight:500;font-size:26px">Lorm Ipsum Dolor Siet</span>
</div>
<div class="photo" role="img" aria-label="Excavator digging in a suburban garden" style="left:577px;top:3128px;width:219px;height:201px;background:linear-gradient(180deg,#9cb8c8,#5f8a3e 55%,#7a5a3a)"></div>
<div class="photo" role="img" aria-label="Excavator at a building site beneath green hills" style="left:809px;top:3128px;width:278px;height:201px;background:linear-gradient(180deg,#a9c9e6,#4f7a3a 50%,#8a7050)"></div>
<div class="photo" role="img" aria-label="Excavator working in a pine forest" style="left:577px;top:3342px;width:279px;height:202px;background:linear-gradient(180deg,#6b7d6a,#2f4a2e 50%,#6a5030)"></div>
<div class="photo" role="img" aria-label="Excavator in lush green woodland" style="left:868px;top:3342px;width:219px;height:202px;background:linear-gradient(180deg,#7fae4a,#3e6a2a 55%,#5a4a28)"></div>

<footer class="footer">
  <div class="brand" style="left:102px;top:80px;color:#fff"><span class="brand-mark"></span>Kolbane Ridge</div>
  <div class="abs" style="left:111px;top:158px;width:341px;height:50px;background:#fff;color:#777;font-size:13px;padding:16px 14px">Enter email addresss</div>
  <a class="btn" href="#" style="left:111px;top:221px;width:135px;height:46px;font-size:15px;font-weight:400">SUBSCRIBE</a>

  <h4 style="left:526px;top:85px">Quick Links</h4>
  <ul style="left:526px;top:122px"><li>Home</li><li>About Us</li><li>Service</li><li>Projects</li><li>Contact Us</li></ul>
  <h4 style="left:706px;top:85px">Other Links</h4>
  <ul style="left:706px;top:122px"><li>Privacy Policy</li><li>Terms &amp; Conditions</li><li>FAQ’s</li><li>Suport</li><li>Help</li></ul>
  <h4 style="left:889px;top:85px">Contact Info</h4>
  <div class="contact-row" style="top:144px"><i><svg width="12" height="14" viewBox="0 0 12 14"><path d="M6 0a5 5 0 0 1 5 5c0 4-5 9-5 9S1 9 1 5a5 5 0 0 1 5-5z" fill="#111"/><circle cx="6" cy="5" r="2" fill="#fff"/></svg></i>Welshpool WA 6106, Australia</div>
  <div class="contact-row" style="top:199px"><i><svg width="14" height="14" viewBox="0 0 14 14"><path d="M3 1l3 3-2 2c1 2 2 3 4 4l2-2 3 3-2 2C6 13 1 8 1 3z" fill="#111"/></svg></i>+61 8 9000 4172</div>
  <div class="contact-row" style="top:253px"><i><svg width="14" height="10" viewBox="0 0 14 10"><rect x="0.5" y="0.5" width="13" height="9" fill="none" stroke="#111"/><path d="M1 1l6 5 6-5" stroke="#111" fill="none"/></svg></i>kolbaneridgeworks.com.au</div>

  <div class="abs" style="left:110px;top:339px;width:974px;height:1px;background:#666"></div>
  <div class="abs" style="left:0;top:354px;width:1200px;text-align:center;font-size:15px">© 2026 &nbsp; Kolbane Ridge Earthworks. All rights reserved.</div>
</footer>
<span class="social" aria-label="Social link" style="left:113px;background:var(--lime)"></span>
<span class="social" aria-label="Social link" style="left:149px"></span>
<span class="social" aria-label="Social link" style="left:185px"></span>
<span class="social" aria-label="Social link" style="left:222px"></span>

</body>
</html>
```